Brightpath Coverage Partners
Stationary
Project: Brightpath Coverage Partners
Brightpath Coverage Partners -
Creative Brief
Professional
Dorian Fell
Agent / Broker
71362 West Maple Lane Ste. B Larkmere, CA 92871-0517
dorian@brightpathcoverage.example
www.brightpathcoverage.example
Insurance License No: 0K72918
Please put the main lines of insurance I sell: Home, Auto, Commercial, Life, Health, Retirement

```html
<!DOCTYPE html>
<html lang="en">
<head>
<meta charset="utf-8">
<title>Brightpath Coverage Partners — Stationery</title>
<link href="https://fonts.googleapis.com/css2?family=Tinos:wght@400;700&display=swap" rel="stylesheet">
<style>
  :root {
    --navy: #0d2a6b;
    --blue: #1f4fa8;
    --sky: #5f86cf;
    --steel: #8a93a3;
    --ink: #2a2f3a;
    --link: #2f5fc0;
    --paper: #ffffff;
    --bg: #ffffff;
    --edge: #d4d7dd;
  }
  * { box-sizing: border-box; margin: 0; padding: 0; }
  html, body { width: 1200px; height: 768px; overflow: hidden; background: var(--bg); }
  body { position: relative; font-family: "Tinos", "Times New Roman", serif; color: var(--ink); }

  .sheet { position: absolute; background: var(--paper); border: 1px solid var(--edge); box-shadow: 0 2px 5px rgba(0,0,0,.12); overflow: hidden; }
  .sheet svg.header { position: absolute; left: 0; top: 0; display: block; }

  .brand { position: absolute; display: flex; flex-direction: column; align-items: center; color: var(--navy); font-weight: 700; text-transform: uppercase; text-align: center; line-height: 1; }
  .brand-mark { background: var(--navy); border-radius: 3px; }
  address { font-style: normal; }

  /* letterhead */
  .letterhead { left: 29px; top: 36px; width: 554px; height: 696px; }
  .letterhead .brand { left: 18px; top: 54px; width: 210px; }
  .letterhead .brand-mark { width: 34px; height: 34px; margin-bottom: 10px; }
  .letterhead .brand-name { font-size: 20px; letter-spacing: .5px; line-height: 1.1; }
  .letterhead .contact { position: absolute; left: 22px; bottom: 18px; font-size: 10.5px; line-height: 1.55; color: var(--ink); }
  .contact .link { color: var(--link); }

  /* business cards */
  .card { top: 163px; width: 245px; height: 125px; }
  .card-front { left: 629px; }
  .card-back { left: 893px; }
  .card .brand { top: 22px; }
  .card-front .brand { left: 50px; width: 145px; }
  .card-front .brand-mark { width: 16px; height: 16px; margin-bottom: 4px; }
  .card-front .brand-name { font-size: 10px; line-height: 1.1; }
  .card-front .lines { position: absolute; left: 14px; bottom: 18px; font-size: 7.5px; color: var(--steel); letter-spacing: .2px; }
  .card-back .brand { left: 8px; width: 92px; }
  .card-back .brand-mark { width: 12px; height: 12px; margin-bottom: 3px; }
  .card-back .brand-name { font-size: 6.5px; line-height: 1.1; }
  .card-back .person { position: absolute; left: 150px; top: 48px; }
  .person-name { font-size: 10px; color: var(--ink); }
  .person-title { font-size: 5.5px; color: var(--steel); }
  .card-back .contact { position: absolute; left: 12px; bottom: 14px; font-size: 5.5px; line-height: 1.5; }

  /* envelope */
  .envelope { left: 629px; top: 391px; width: 511px; height: 319px; }
  .envelope .brand { left: 14px; top: 130px; width: 150px; }
  .envelope .brand-mark { width: 26px; height: 26px; margin-bottom: 7px; }
  .envelope .brand-name { font-size: 14px; line-height: 1.1; }
  .envelope .return { position: absolute; left: 22px; top: 218px; font-size: 8.5px; line-height: 1.45; }
  .envelope .flap-mark { position: absolute; left: 242px; top: 30px; width: 30px; height: 30px; border: 2px solid var(--paper); border-radius: 6px; }
</style>
</head>
<body>

<section class="sheet letterhead" aria-label="Letterhead">
  <svg class="header" width="554" height="70" viewBox="0 0 554 70" aria-hidden="true">
    <defs>
      <linearGradient id="lh-band" x1="0" y1="0" x2="1" y2="0">
        <stop offset="0" stop-color="#0d2a6b"/><stop offset=".55" stop-color="#1f4fa8"/><stop offset="1" stop-color="#5f86cf"/>
      </linearGradient>
    </defs>
    <rect width="554" height="44" fill="url(#lh-band)"/>
    <rect y="44" width="554" height="4" fill="#8a93a3"/>
    <path d="M78 48 V30 Q78 14 96 14 H150 Q168 14 168 30 V48 Z" fill="#ffffff"/>
  </svg>
  <div class="brand">
    <span class="brand-mark"></span>
    <span class="brand-name">Brightpath<br>Coverage Partners</span>
  </div>
  <address class="contact">
    71362 West Maple Lane Ste. B, Larkmere, CA 92871-0517<br>
    Phone: 555.201.0142 | Cell: 555.201.0187 | Fax: 555.201.0163<br>
    Email: <span class="link">dorian@brightpathcoverage.example</span> · Web: <span class="link">www.brightpathcoverage.example</span><br>
    License No.: 0K72918
  </address>
</section>

<section class="sheet card card-front" aria-label="Business card front">
  <svg class="header" width="245" height="30" viewBox="0 0 245 30" aria-hidden="true">
    <defs>
      <linearGradient id="cf-band" x1="0" y1="0" x2="1" y2="0">
        <stop offset="0" stop-color="#0d2a6b"/><stop offset=".6" stop-color="#1f4fa8"/><stop offset="1" stop-color="#5f86cf"/>
      </linearGradient>
    </defs>
    <rect width="245" height="22" fill="url(#cf-band)"/>
    <rect y="22" width="245" height="2" fill="#8a93a3"/>
    <path d="M104 24 V16 Q104 8 112 8 H133 Q141 8 141 16 V24 Z" fill="#ffffff"/>
  </svg>
  <div class="brand">
    <span class="brand-mark"></span>
    <span class="brand-name">Brightpath<br>Coverage Partners</span>
  </div>
  <p class="lines">Home, Auto, Commercial, Life, Health, Retirement</p>
</section>

<section class="sheet card card-back" aria-label="Business card back">
  <svg class="header" width="245" height="30" viewBox="0 0 245 30" aria-hidden="true">
    <defs>
      <linearGradient id="cb-band" x1="0" y1="0" x2="1" y2="0">
        <stop offset="0" stop-color="#0d2a6b"/><stop offset=".6" stop-color="#1f4fa8"/><stop offset="1" stop-color="#5f86cf"/>
      </linearGradient>
    </defs>
    <rect width="245" height="22" fill="url(#cb-band)"/>
    <rect y="22" width="245" height="2" fill="#8a93a3"/>
    <path d="M38 24 V16 Q38 9 45 9 H62 Q69 9 69 16 V24 Z" fill="#ffffff"/>
  </svg>
  <div class="brand">
    <span class="brand-mark"></span>
    <span class="brand-name">Brightpath<br>Coverage Partners</span>
  </div>
  <div class="person">
    <p class="person-name">Dorian Fell</p>
    <p class="person-title">Agent / Broker</p>
  </div>
  <address class="contact">
    71362 West Maple Lane Ste. B, Larkmere, CA 92871-0517<br>
    Phone: 555.201.0142 | Cell: 555.201.0187 | Fax: 555.201.0163<br>
    Email: <span class="link">dorian@brightpathcoverage.example</span><br>
    Web: <span class="link">www.brightpathcoverage.example</span><br>
    License No.: 0K72918
  </address>
</section>

<section class="sheet envelope" aria-label="Envelope">
  <svg class="header" width="511" height="130" viewBox="0 0 511 130" aria-hidden="true">
    <defs>
      <linearGradient id="env-flap" x1="0" y1="0" x2="0" y2="1">
        <stop offset="0" stop-color="#0d2a6b"/><stop offset=".7" stop-color="#1f4fa8"/><stop offset="1" stop-color="#4a72c0"/>
      </linearGradient>
    </defs>
    <path d="M0 0 H511 V88 L300 88 Q257 120 214 88 L0 88 Z" fill="url(#env-flap)"/>
    <path d="M0 88 L214 88 Q257 120 300 88 L511 88 V93 L302 93 Q257 126 212 93 L0 93 Z" fill="#8a93a3"/>
  </svg>
  <span class="flap-mark"></span>
  <div class="brand">
    <span class="brand-mark"></span>
    <span class="brand-name">Brightpath<br>Coverage Partners</span>
  </div>
  <address class="return">
    71362 West Maple Lane Ste. B<br>
    Larkmere, CA 92871-0517
  </address>
</section>

</body>
</html>
```